Cloudvane MarketHub (appstore) Billboards - Dealcadence

We offer an app on the Cloudvane MarketHub - B2B app store which is called Dealcadence. We have a presentation of our application consisting of 15 billboards with information and graphics about our application. I want a new design for our Billboards and want to have the first 5 created.

Here is our App listing and when you click on the big image you see the billboards I want to create. The first 5 is enough and I also want the template so I can create more myself.
I have added a ppt with lots of screenshots of the application

Each image/Billboard must follow these specs Specs: 700x467 pixel jpg or png no larger than 1MB

https://markethub.cloudvane-example.com/listingView?itemRef=k7R9T22222MBqzLXPQ

Here is a video about what the Dealcadence app does

Target Market(s)

Cloudvane customers , Sales Executives, VP Sales , Sales operations - Relevant for all industries that run a sales process based on customer meetings and/or phone meetings

Colors

Designer to choose colors to be used in the design.

Requirements
Must have
• Screenshots from the solution. The billboards is to spike interest from people viewing and also showcase how things look inside their Cloudvane solution with our Dealcadence app running
• - SEE EXAMPLE Billboard image of what type of Billboard I am after

```html
<!DOCTYPE html>
<html lang="en">
<head>
<meta charset="UTF-8">
<title>Dealcadence Billboard – Reconnect Based On Feedback</title>
<link rel="stylesheet" href="https://fonts.googleapis.com/css2?family=Lexend:wght@300;400;600;700&display=swap">
<style>
  :root {
    --page: #ffffff;
    --navy: #07066b;
    --yellow: #ffee00;
    --body-text: #d3d9ef;
    --bullet: #4aa3a0;
    --orange: #ff6a00;
    --white: #ffffff;
    --screen-fill: #f4f6fa;
    --frame: #4a4a55;
  }
  html, body {
    margin: 0;
    padding: 0;
    width: 1200px;
    height: 1200px;
    overflow: hidden;
    background: var(--page);
  }
  .billboard {
    position: absolute;
    left: 210px;
    top: 339px;
    width: 781px;
    height: 523px;
    background: var(--navy);
    outline: 1px solid var(--frame);
    overflow: hidden;
    font-family: "Lexend", sans-serif;
  }
  .screen-shape {
    position: absolute;
    inset: 0;
    width: 781px;
    height: 523px;
  }
  .headline {
    position: absolute;
    left: 27px;
    top: 50px;
    width: 390px;
    margin: 0;
    color: var(--yellow);
    font-weight: 600;
    font-size: 31px;
    line-height: 37px;
    letter-spacing: -0.2px;
  }
  .benefits {
    position: absolute;
    left: 60px;
    top: 174px;
    width: 342px;
    margin: 0;
    padding: 0;
    list-style: none;
    color: var(--body-text);
    font-weight: 300;
    font-size: 20px;
    line-height: 25.6px;
    text-align: justify;
  }
  .benefits li {
    position: relative;
  }
  .benefits li::before {
    content: "";
    position: absolute;
    left: -32px;
    top: 11px;
    width: 5px;
    height: 5px;
    border-radius: 50%;
    background: var(--bullet);
  }
  .call-to-action {
    position: absolute;
    left: 27px;
    top: 412px;
    margin: 0;
    font-weight: 600;
    font-size: 22px;
    color: var(--white);
  }
  .call-to-action span {
    display: block;
    width: max-content;
    background: var(--orange);
    padding: 0 8px;
    height: 33px;
    line-height: 35px;
    margin-bottom: 3px;
  }
  .brand {
    position: absolute;
    right: 35px;
    top: 430px;
    text-align: right;
    color: var(--white);
  }
  .brand-row {
    display: flex;
    align-items: center;
    gap: 8px;
  }
  .brand-dot {
    width: 36px;
    height: 36px;
    border-radius: 50%;
    background: var(--white);
  }
  .brand-name {
    font-weight: 600;
    font-size: 29px;
    line-height: 36px;
  }
  .brand-tagline {
    font-weight: 400;
    font-size: 8px;
    margin-top: 2px;
  }
</style>
</head>
<body>
  <section class="billboard">
    <svg class="screen-shape" viewBox="0 0 781 523" role="img" aria-label="Screenshot of a CRM feedback notification showing a customer's meeting evaluation scores">
      <path fill="var(--screen-fill)" d="M605 0 C585 22 570 38 548 45 C505 58 470 70 448 100 C420 130 405 150 418 172 C428 192 470 205 494 240 C505 265 480 300 498 320 C515 345 560 350 640 358 C700 364 725 372 735 388 C750 400 768 405 781 409 L781 0 Z"/>
    </svg>

    <h1 class="headline">Increase The Chance of Closing By Reconnecting Based On The Feedback</h1>

    <ul class="benefits">
      <li>Detect shortcomings with the prospect immediately and reconnect</li>
      <li>Sales reps can better understand their strengths and weaknesses as perceived by their prospects and customers</li>
    </ul>

    <p class="call-to-action">
      <span>GIVE YOUR SALES TEAM A TOOL</span>
      <span>FOR SELF-DEVELOPMENT</span>
    </p>

    <div class="brand">
      <div class="brand-row">
        <div class="brand-dot"></div>
        <div class="brand-name">Dealcadence</div>
      </div>
      <div class="brand-tagline">A Northfeld Company</div>
    </div>
  </section>
</body>
</html>
```